lunetra.com redesign

We are a successful web hosting company that has been around since 1999 with 10,000 customers managing 2,000 websites and 12,000 domain names. Our challenge - we are losing ground because our site is getting old, our pricing is not competitive and our feature set needs to change to match the new world of mobile centric everything. We want to reach out to all of the domain names that we don't host websites for. We believe that if we designed a new site that focuses on bringing home all of those externally hosted websites to our own web hosting company that we would have a solid future. We need to compete against mopwizzle.com, vantrimble.com, kerbloom.com, zinqhut.com, nolvark.com, brimfolk.com, quorvane.com, welbix.com and 100,000 others. We need to simplify our message with clean design, focused pages, easy decision making processes for the consumer. We use WHMCS for the background provisioning and billing so we can pretty much manage any kind of pricing model and discounted promotion packages.
I would prefer Twitter bootstrap CSS based responsive design.

Reason: I was away on vacation for 2 weeks - I just got back - I need time to fairly review all submissions - thank you for your patience. Dorian Fenwick Lunetra.com

Thanks to all who submitted sample designs - unfortunately most of them were nothing much more than already available templates with some of my current content and logo added to them. I will try to be more specific to reduce the number of choices. I need the template be fully compatible with WHMCS and Pagewright if you can't make it work with WHMCS directly. Another question I have to ask is -"exactly what am I getting for my $500.00 - is it just a PSD template or actual integration of that theme into WHMCS or Pagewright?"  I don't expect anyone to create new content for the site at that price. What do you charge if  you are able to create content or get directly involved in the site implementation of that template?

```html
<!DOCTYPE html>
<html lang="en">
<head>
<meta charset="utf-8">
<title>Lunetra – Reliable Web Hosting</title>
<link href="https://fonts.googleapis.com/css2?family=Oswald:wght@400;500;600&family=Open+Sans:ital,wght@0,400;0,600;0,700;1,400;1,700&display=swap" rel="stylesheet">
<style>
:root{
  --brand:#1f7fb8;
  --dark:#3a3a3a;
  --darker:#2b2b2b;
  --footer:#3d3d3d;
  --hero-a:#1f6f9e;
  --hero-b:#3a9ac8;
  --orange:#e9902a;
  --blue:#4f87a8;
  --green:#3dc83a;
  --red:#d8393f;
  --yellow:#e8b32b;
  --promo-green:#7cbc4a;
  --promo-blue:#4a8ac2;
  --promo-red:#e8432c;
  --text:#555;
  --light:#f6f6f6;
}
*{box-sizing:border-box;margin:0;padding:0}
html,body{width:800px;height:1200px;overflow:hidden}
body{position:relative;font-family:"Open Sans",sans-serif;color:var(--text);background:#fff}
.abs{position:absolute}

/* header */
.header{position:absolute;left:0;top:0;width:800px;height:66px;background:#fff}
.logo{position:absolute;left:72px;top:10px;font:600 40px/1 "Open Sans",sans-serif;color:var(--brand);letter-spacing:-1px}
.field{position:absolute;top:10px;height:17px;border:1px solid #ccc;font-size:8px;color:#999;padding:3px 6px;background:#fafafa}
.login-note{position:absolute;left:540px;top:35px;font-size:8.5px;line-height:12px;text-align:right;width:122px;color:#555}
.login-note u{color:#333}
.login-btn{position:absolute;left:678px;top:38px;width:55px;height:17px;background:var(--brand);color:#fff;font-size:9px;text-align:center;line-height:17px;border-radius:2px}

/* nav */
.nav{position:absolute;left:0;top:66px;width:800px;height:28px;background:var(--dark);border-bottom:1px solid #222}
.nav a{position:absolute;top:0;line-height:28px;color:#fff;font-size:10px;text-decoration:none;font-family:Arial,sans-serif}
.nav .sep{position:absolute;top:6px;width:1px;height:16px;background:#555}

/* hero */
.hero{position:absolute;left:0;top:94px;width:800px;height:314px;background:radial-gradient(ellipse at 55% 30%,var(--hero-b),var(--hero-a) 75%)}
.hero h1{position:absolute;left:66px;top:40px;font:600 29px/1 "Oswald",sans-serif;color:#fff;letter-spacing:.3px}
.hero .sub{position:absolute;left:66px;top:78px;width:300px;font-size:13px;line-height:16px;color:#fff}
.bullets{position:absolute;left:66px;top:134px;list-style:none}
.bullets li{height:23px;font-size:10.5px;color:#fff;padding-left:21px;position:relative}
.bullets li::before{content:"›";position:absolute;left:0;top:1px;width:11px;height:11px;border-radius:50%;background:#fff;color:var(--brand);font-size:11px;line-height:9px;text-align:center;font-weight:700}
.hero-btn{position:absolute;top:259px;width:120px;height:33px;color:#fff;font-size:10px;font-weight:600;line-height:33px;border-radius:2px;box-shadow:0 1px 2px rgba(0,0,0,.35)}
.hero-btn .ic{position:absolute;left:0;top:0;width:33px;height:33px;text-align:center;font-size:14px}
.hero-btn span.t{position:absolute;left:46px}
.btn-dark{left:66px;background:#4a4a4a}
.btn-dark .ic{background:#2e2e2e}
.btn-blue{left:198px;background:#1f6fc0}
.btn-blue .ic{background:#1a5ea6}
.servers{position:absolute;left:356px;top:46px;width:376px;height:220px;background:linear-gradient(180deg,#dfe4e8,#8d959b 70%,#5c6368);border-radius:6px;opacity:.9}

/* domain search */
.domain{position:absolute;left:0;top:408px;width:800px;height:72px;background:var(--dark)}
.domain h2{position:absolute;left:66px;top:21px;font:400 20px/1.3 "Oswald",sans-serif;color:#fff}
.domain .input{position:absolute;left:267px;top:21px;width:303px;height:29px;background:#fff}
.search-btn{position:absolute;left:582px;top:19px;width:119px;height:33px;background:#5a5a5a;border-radius:2px;color:#fff;font:400 14px/33px "Oswald",sans-serif}
.search-btn .ic{position:absolute;left:0;top:0;width:33px;height:33px;background:#1a5ea6;text-align:center;font-size:14px}
.search-btn span.t{position:absolute;left:48px;letter-spacing:.5px}

/* pricing */
.pricing{position:absolute;left:0;top:480px;width:800px;height:314px;background:var(--light)}
.plan{position:absolute;top:22px;width:157px;height:268px;background:#fff;border:1px solid #e3e3e3}
.plan .head{height:28px;background:linear-gradient(#4a4a4a,#333);color:#fff;text-align:center;font:500 11.5px/28px "Oswald",sans-serif}
.plan svg.ribbon{display:block}
.plan .price{position:absolute;left:0;top:36px;width:157px;text-align:center;color:#fff;font:600 22px/1 "Oswald",sans-serif}
.plan .per{position:absolute;left:0;top:62px;width:157px;text-align:center;color:#fff;font-size:6.5px;font-weight:700}
.plan ul{list-style:none;position:absolute;left:18px;top:99px;width:124px}
.plan li{height:19.4px;font-size:8.5px;line-height:19.4px;border-bottom:1px solid #f0f0f0;padding-left:12px;position:relative}
.plan li:last-child{border-bottom:0}
.plan li::before{content:"✓";position:absolute;left:0;top:0;font-weight:700;font-size:8px}
.plan li b{color:#444}
.plan .sign{position:absolute;left:41px;top:228px;width:74px;height:24px;color:#fff;text-align:center;font:500 9px/24px "Oswald",sans-serif;border-radius:2px}
.p-orange li::before{color:var(--orange)} .p-orange .sign{background:var(--orange)}
.p-blue li::before{color:var(--blue)} .p-blue .sign{background:var(--blue)}
.p-green li::before{color:var(--green)} .p-green .sign{background:var(--green)}
.p-red li::before{color:var(--red)} .p-red .sign{background:var(--red)}
.badge{position:absolute;left:122px;top:3px;width:30px;height:30px;border-radius:50%;background:#f3d21c;color:#333;font:700 5.5px/6px "Open Sans",sans-serif;text-align:center;padding-top:9px}

/* promos */
.promos{position:absolute;left:0;top:794px;width:800px;height:211px;background:#e6e6e6}
.promo{position:absolute;top:39px;width:157px;height:132px;background:radial-gradient(circle at 40% 40%,#555,#383838);border-radius:3px;box-shadow:0 2px 3px rgba(0,0,0,.35)}
.promo::after{content:"";position:absolute;inset:4px;border:1px dashed #6d6d6d;border-radius:2px;pointer-events:none}
.promo .title{position:absolute;left:11px;top:13px;color:#fff;font:italic 700 17px/21px "Open Sans",sans-serif;letter-spacing:.5px}
.promo .title em{display:block;font-weight:400;letter-spacing:1px}
.promo .desc{position:absolute;left:11px;top:62px;width:84px;color:#eee;font-size:7.2px;line-height:12px;white-space:nowrap}
.promo .art{position:absolute;right:10px;bottom:12px;width:48px;height:46px;border-radius:6px;background:linear-gradient(135deg,#c9d6e2,#6d8faa)}
.promo .coin{position:absolute;top:-14px;right:-6px;width:64px;height:64px;border-radius:50%;border:3px solid rgba(255,255,255,.85);color:#fff;text-align:center;font:700 16px/17px "Open Sans",sans-serif;padding-top:13px;box-shadow:0 1px 3px rgba(0,0,0,.3)}

/* footer */
.footer{position:absolute;left:0;top:1005px;width:800px;height:168px;background:var(--footer)}
.fcol{position:absolute;top:21px}
.fcol h3{font:600 13px/1 "Open Sans",sans-serif;color:#fff;margin-bottom:15px;letter-spacing:-.2px}
.fcol a{display:block;color:#fff;font-size:9px;text-decoration:none;height:20px}
.fsep{position:absolute;top:22px;width:1px;height:120px;background:#4a4a4a}
.social a{padding-left:26px;position:relative;height:26.5px;line-height:16px}
.social a i{position:absolute;left:0;top:0;width:16px;height:16px;border-radius:2px}
.contact div{color:#fff;font-size:9px;line-height:12px;padding-left:19px;position:relative;margin-bottom:11px}
.contact svg{position:absolute;left:0;top:1px}
.cards{position:absolute;left:606px;top:140px}
.cards span{display:inline-block;width:21px;height:13px;background:#fff;border-radius:1px;margin-right:3px;font-size:5.5px;font-weight:700;color:#234;text-align:center;line-height:13px}
.bottom{position:absolute;left:0;top:1173px;width:800px;height:27px;background:var(--darker);color:#fff;font-size:9px;line-height:27px}
.bottom .copy{position:absolute;left:69px}
.bottom .links{position:absolute;right:72px;font-size:8px;color:#bbb}
</style>
</head>
<body>

<header class="header">
  <div class="logo">lunetra</div>
  <div class="field" style="left:504px;width:110px">Username</div>
  <div class="field" style="left:629px;width:104px">Password</div>
  <div class="login-note">Forgot login?<br>No account yet? <u>Register</u></div>
  <div class="login-btn">LOGIN</div>
</header>

<nav class="nav">
  <svg class="abs" style="left:78px;top:7px" width="15" height="13" viewBox="0 0 15 13" aria-hidden="true"><path d="M7.5 0 0 6.5h2V13h4V9h3v4h4V6.5h2z" fill="#fff"/></svg>
  <span class="sep" style="left:100px"></span>
  <a style="left:109px">DOMAIN NAME CENTER</a><span class="sep" style="left:230px"></span>
  <a style="left:246px">WEB SITE HOSTING CENTER</a><span class="sep" style="left:390px"></span>
  <a style="left:406px">S.E.O. TOOLKIT</a><span class="sep" style="left:490px"></span>
  <a style="left:506px">SUPPORT</a><span class="sep" style="left:566px"></span>
  <a style="left:582px">CLIENT AREA</a><span class="sep" style="left:660px"></span>
  <a style="left:674px">CONTACT US</a>
</nav>

<section class="hero">
  <h1>RELIABLE WEB HOSTING</h1>
  <p class="sub">simply dummy text of the printing and typesetting industry.</p>
  <ul class="bullets">
    <li>Unlimited Bandwidth with Massive Storage</li>
    <li>Unlimited Databases and Email Addresses</li>
    <li>Apps Including Pagewright, Nodeleaf and Stackly</li>
    <li>Unlimited Bandwidth with Massive Storage</li>
    <li>Apps Including Pagewright, Nodeleaf and Stackly</li>
  </ul>
  <div class="hero-btn btn-dark"><span class="ic">➔</span><span class="t">VIEW DETAILS</span></div>
  <div class="hero-btn btn-blue"><span class="ic">☞</span><span class="t">SIGN UP NOW</span></div>
  <div class="servers" role="img" aria-label="Row of silver server towers"></div>
</section>

<section class="domain">
  <h2>Enter a Domain Name:</h2>
  <div class="input"></div>
  <div class="search-btn"><span class="ic">➔</span><span class="t">SEARCH</span></div>
</section>

<section class="pricing">
  <div class="plan p-orange" style="left:66px">
    <div class="head">STANDARD PLAN</div>
    <svg class="ribbon" width="155" height="54" viewBox="0 0 155 54"><polygon points="0,0 155,0 155,36 77.5,54 0,36" fill="var(--orange)"/></svg>
    <div class="price">$2.99</div><div class="per">per month</div>
    <ul><li><b>500 GB</b> Disk Space</li><li>100 Databases List</li><li><b>Free Domain</b> Registration</li><li>1 Hosting Space</li><li>Account Control Panel</li><li>FREE 24/7 Support</li></ul>
    <div class="sign">SIGN UP NOW</div>
  </div>
  <div class="plan p-blue" style="left:236px">
    <div class="head">PROFESSIONAL PLAN</div>
    <svg class="ribbon" width="155" height="54" viewBox="0 0 155 54"><polygon points="0,0 155,0 155,36 77.5,54 0,36" fill="var(--blue)"/></svg>
    <div class="price">$4.99</div><div class="per">per month</div>
    <ul><li><b>Unlimited</b> Disk Space</li><li>100 Databases List</li><li><b>Free Domain</b> Registration</li><li>1 Hosting Space</li><li>Account Control Panel</li><li>FREE 24/7 Support</li></ul>
    <div class="sign">SIGN UP NOW</div>
  </div>
  <div class="plan p-green" style="left:406px">
    <div class="head">ADVANCED PLAN</div>
    <div class="badge">BEST<br>VALUE</div>
    <svg class="ribbon" width="155" height="54" viewBox="0 0 155 54"><polygon points="0,0 155,0 155,36 77.5,54 0,36" fill="var(--green)"/></svg>
    <div class="price">$27.99</div><div class="per">per month</div>
    <ul><li><b>Unlimited</b> Disk Space</li><li>100 Databases List</li><li><b>Free Domain</b> Registration</li><li>1 Hosting Space</li><li>Account Control Panel</li><li>FREE 24/7 Support</li></ul>
    <div class="sign">SIGN UP NOW</div>
  </div>
  <div class="plan p-red" style="left:575px">
    <div class="head">UNLIMITED PLAN</div>
    <svg class="ribbon" width="155" height="54" viewBox="0 0 155 54"><polygon points="0,0 155,0 155,36 77.5,54 0,36" fill="var(--red)"/></svg>
    <div class="price">$99.99</div><div class="per">per month</div>
    <ul><li><b>Unlimited</b> Disk Space</li><li>100 Databases List</li><li><b>Free Domain</b> Registration</li><li>1 Hosting Space</li><li>Account Control Panel</li><li>FREE 24/7 Support</li></ul>
    <div class="sign">SIGN UP NOW</div>
  </div>
</section>

<section class="promos">
  <div class="promo" style="left:66px">
    <div class="title">EASY<em>Transfer</em></div>
    <p class="desc"><b>Unlimited</b> Data trans-<br>fer Easy Control Panel<br>Web Based stats<br>TableDB &amp; Qwip</p>
    <div class="art" role="img" aria-label="Server rack with operating system stickers"></div>
    <div class="coin" style="background:var(--promo-red)">$108<br>yr.</div>
  </div>
  <div class="promo" style="left:236px">
    <div class="title">SITE<em>Builder</em></div>
    <p class="desc"><b>Unlimited</b> Data trans-<br>fer Easy Control Panel<br>Web Based stats<br>TableDB &amp; Qwip</p>
    <div class="art" role="img" aria-label="Folder with a globe"></div>
    <div class="coin" style="background:var(--yellow)">$108<br>yr.</div>
  </div>
  <div class="promo" style="left:406px">
    <div class="title">Install<em>atron</em></div>
    <p class="desc"><b>Unlimited</b> Data trans-<br>fer Easy Control Panel<br>Web Based stats<br>TableDB &amp; Qwip</p>
    <div class="art" role="img" aria-label="Envelope with a blue arrow"></div>
    <div class="coin" style="background:var(--promo-green)">$108<br>yr.</div>
  </div>
  <div class="promo" style="left:572px">
    <div class="title">BE<em>Founder</em></div>
    <p class="desc" style="top:68px"><b>Unlimited</b> Data trans-<br>fer Easy Control Panel<br>Web Based stats<br>TableDB &amp; Qwip</p>
    <div class="art" role="img" aria-label="Red no-entry sign over an envelope" style="background:linear-gradient(135deg,#f1f1f1,#c63a3a)"></div>
    <div class="coin" style="background:var(--promo-blue)">$108<br>yr.</div>
  </div>
</section>

<footer class="footer">
  <div class="fcol" style="left:67px"><h3>Lunetra Host</h3><a>Home</a><a>About Us</a><a>Cloud Server</a><a>Domain</a><a>Contact Us</a></div>
  <span class="fsep" style="left:160px"></span>
  <div class="fcol" style="left:178px"><h3>Help &amp; Support</h3><a>FAQ.s</a><a>Live Support</a><a>Support Ticket</a></div>
  <span class="fsep" style="left:295px"></span>
  <div class="fcol" style="left:321px"><h3>My account</h3><a>Sign In</a><a>View Cart</a><a>My Wishlist</a><a>Track My Order</a><a>Help</a></div>
  <span class="fsep" style="left:433px"></span>
  <div class="fcol social" style="left:463px"><h3>Social Connection</h3>
    <a><i style="background:#3b5a98"></i>Chatterbox</a>
    <a><i style="background:#3fb3e6"></i>View Cart</a>
    <a><i style="background:#555"></i>My Wishlist</a>
    <a><i style="background:#c9302c"></i>Track My Order</a>
  </div>
  <span class="fsep" style="left:575px"></span>
  <div class="fcol contact" style="left:606px"><h3>Get in Touch</h3>
    <div><svg width="8" height="11" viewBox="0 0 8 11" aria-hidden="true"><rect x=".5" y=".5" width="7" height="10" rx="1" fill="none" stroke="#fff"/><circle cx="4" cy="8.7" r=".8" fill="#fff"/></svg>(+1) 555 014 2290</div>
    <div><svg width="11" height="9" viewBox="0 0 11 9" aria-hidden="true"><rect x=".5" y=".5" width="10" height="8" fill="none" stroke="#fff"/><path d="M.5.5 5.5 5l5-4.5" fill="none" stroke="#fff"/></svg>info@lunetrahost.com</div>
    <div><svg width="9" height="12" viewBox="0 0 9 12" aria-hidden="true"><path d="M4.5 0A4.5 4.5 0 0 0 0 4.5C0 8 4.5 12 4.5 12S9 8 9 4.5A4.5 4.5 0 0 0 4.5 0z" fill="#fff"/><circle cx="4.5" cy="4.5" r="1.6" fill="#3d3d3d"/></svg>Lunetra Host Ltd, Harbor Row<br>42, Westfield, USA</div>
  </div>
  <div class="cards"><span>VELO</span><span>MIRA</span><span>DINERO</span><span>AXIS</span><span>PAYLO</span></div>
</footer>

<div class="bottom">
  <span class="copy">Copyright © 2013 Lunetra. All Rights Reserved.</span>
  <span class="links">Privacy Policy | Terms &amp; Condition</span>
</div>

</body>
</html>
```